Beautiful e-comm site for 'roadside farmers stand' online!

Need a logo design and basic e-comm website (super super simple) for new business called Brindlecove. Brindlecove is an online farmers stand where local artisans can sell 'brindlecove' goods directly from their makers!

Looking for something simple, whimsicle and clean! (Ideally with a light grey or perrywinkle and some color mixed in - word 'Brindlecove' in black - can work the pear shape in somewhere but not required!)

Target Market(s)

Hobby shoppers and 'quilo' goers who want a focus on edible things and care about ingredients!

Industry/Entity Type

E-Commerce

Number of Pages Required

2 page

Font styles to use
Decorative
Script

Colors
f3f1f8
ec1f27
cadf82

Requirements
Must have
• - Basic logo
• - Homepage
• - Product Detail Page
• - Be in a responsive, woocommerce or shopify, wordpress theme (will purchase theme after design is approved)
Nice to have
• - Matching check out & cart pages
• - 'About Us' page
• - SEO plugin
Should not have
• A cluttered look/feel.

```html
<!DOCTYPE html>
<html lang="en">
<head>
<meta charset="utf-8">
<title>Brindlecove – online farmers stand</title>
<link rel="stylesheet" href="https://fonts.googleapis.com/css2?family=Mulish:wght@400;600;700;800&family=Montserrat:wght@400;500;600;700&display=swap">
<style>
:root{
  --green:#5b9443;
  --green-dark:#4c7f37;
  --white:#ffffff;
  --card:#f2f2f2;
  --ink:#222222;
  --muted:#7a7a7a;
  --faint:#ececec;
  --star:#f28a1b;
  --footer:#2c2c2c;
}
*{margin:0;padding:0;box-sizing:border-box}
html,body{width:1200px;height:3758px;overflow:hidden;background:var(--white)}
body{position:relative;font-family:"Montserrat",sans-serif;color:var(--ink)}
.abs{position:absolute}
.btn{position:absolute;display:flex;align-items:center;justify-content:center;font-family:"Montserrat",sans-serif;font-weight:600;font-size:17px;letter-spacing:.5px;text-transform:uppercase}
.btn-outline-green{border:3px solid var(--green);color:var(--green);background:var(--white)}
.btn-outline-white{border:3px solid var(--white);color:var(--white)}
.btn-outline-dark{border:3px solid #222;color:#222}
.photo{position:absolute}

/* header */
.hero-panel{left:0;top:0;width:551px;height:689px;background:var(--green)}
.brand{left:55px;top:18px;font-family:"Mulish",sans-serif;font-weight:700;font-size:44px;color:var(--white)}
.nav{left:0;top:36px;width:1200px;height:30px;font-family:"Montserrat",sans-serif;font-size:16px;font-weight:600}
.nav a{position:absolute;text-decoration:none;color:var(--green)}
.nav .active{color:var(--white)}
.nav .active::after{content:"";position:absolute;left:0;right:0;bottom:-8px;height:3px;background:var(--white)}
.signup-top{left:909px;top:28px;width:141px;height:45px;background:var(--green);color:var(--white);font-size:19px}
.cart{left:1103px;top:28px}
.hero-title{left:55px;top:286px;font-family:"Mulish",sans-serif;font-weight:800;font-size:44px;color:var(--white)}
.hero-sub{left:135px;top:336px;font-family:"Mulish",sans-serif;font-weight:700;font-size:37px;color:var(--ink)}
.hero-text{left:55px;top:386px;width:440px;text-align:center;font-size:20px;line-height:30px;color:var(--white)}
.hero-btn{left:180px;top:456px;width:191px;height:47px}
.hero-photo{left:651px;top:150px;width:451px;height:476px;border-radius:45% 45% 30% 30%;background:radial-gradient(circle at 50% 40%,#f2a33a 0%,#d9482b 35%,#6aa23f 60%,#ffffff 75%)}
.vertical{font-family:"Mulish",sans-serif;font-weight:800;color:var(--faint);white-space:nowrap;transform:rotate(-90deg);transform-origin:left top}
.hero-vertical{left:1085px;top:665px;font-size:70px}
.arrow{top:654px;width:37px;height:35px;background:var(--green);display:flex;align-items:center;justify-content:center}

/* promos */
.promo{top:782px;width:530px;height:353px;background:var(--card)}
.promo-heart{left:20px;top:70px;width:240px;height:220px}
.promo-title{right:28px;top:80px;font-family:"Mulish",sans-serif;font-weight:800;font-size:34px;color:var(--green)}
.promo-text{right:28px;top:130px;width:250px;text-align:right;font-size:14px;line-height:27px;color:var(--muted)}
.promo .btn{left:313px;top:230px;width:190px;height:46px}

/* about */
.about-vertical{left:142px;top:1775px;font-size:66px}
.about-photo{left:228px;top:1265px;width:373px;height:504px;background:linear-gradient(180deg,#d9dcd6 0%,#8a7a62 55%,#6a8f45 100%)}
.about-box{left:601px;top:1225px;width:373px;height:586px;background:var(--green)}
.about-title{left:38px;top:72px;font-family:"Mulish",sans-serif;font-weight:800;font-size:40px;color:var(--white)}
.about-title::after{content:"";position:absolute;left:0;bottom:-8px;width:88px;height:3px;background:var(--white)}
.about-text{left:38px;top:143px;width:300px;font-size:14.5px;line-height:28.4px;color:#1f2a19}
.about-box .btn{left:38px;top:456px;width:166px;height:47px}

/* products */
.section-title{left:0;top:1920px;width:1200px;text-align:center;font-family:"Mulish",sans-serif;font-weight:800;font-size:40px;color:var(--green)}
.section-rule{left:525px;top:1977px;width:150px;height:3px;background:var(--green)}
.product{width:360px;height:440px}
.product-photo{left:70px;top:0;width:220px;height:226px;border-radius:40%}
.product-name{left:0;top:270px;width:360px;text-align:center;font-family:"Mulish",sans-serif;font-weight:700;font-size:33px}
.stars{left:105px;top:318px}
.price{left:0;top:377px;font-family:"Mulish",sans-serif;font-weight:700;font-size:30px;font-style:normal}
.product .btn{left:50px;top:369px;width:190px;height:46px}

/* contact */
.contact-panel{left:0;top:3076px;width:614px;height:616px;background:var(--green)}
.contact-title{left:53px;top:55px;font-family:"Mulish",sans-serif;font-weight:800;font-size:42px;color:var(--white)}
.contact-title::after{content:"";position:absolute;left:0;right:0;bottom:-6px;height:3px;background:var(--white)}
.field{left:53px;width:506px;height:46px;border:2px solid #2c3d24;padding:12px 18px;font-size:13px;font-weight:600;color:#2c3d24}
.contact-btn{left:53px;top:494px;width:190px;height:47px;background:var(--white);color:var(--green-dark);font-size:17px}
.contact-brand{left:659px;top:3222px;font-family:"Mulish",sans-serif;font-weight:700;font-size:50px;color:var(--ink)}
.contact-line{left:659px;font-size:16px;font-weight:500;color:var(--ink)}
.social{left:659px;top:3432px;display:flex;gap:10px}
.social span{width:30px;height:30px;border-radius:50%;background:#3a3a3a}
.fruit-photo{left:726px;top:3469px;width:451px;height:223px;background:radial-gradient(ellipse at 75% 45%,#e8eef0 0%,#f4f6f7 30%,#ffffff 70%)}
.footer{left:0;top:3692px;width:1200px;height:66px;background:var(--footer);display:flex;align-items:center;justify-content:center;font-size:15px;font-weight:600;color:var(--green);letter-spacing:.4px}
</style>
</head>
<body>

<header>
  <div class="abs hero-panel"></div>
  <div class="abs brand">Brindlecove</div>
  <nav class="abs nav">
    <a class="active" style="left:363px">Home</a>
    <a style="left:456px;color:var(--white)">About Us</a>
    <a style="left:574px">Products</a>
    <a style="left:694px">Shop</a>
    <a style="left:779px">Contact Us</a>
  </nav>
  <div class="btn signup-top">Sign Up</div>
  <svg class="abs cart" width="44" height="44" viewBox="0 0 44 44" fill="none" stroke="#5b9443" stroke-width="3" stroke-linejoin="round" stroke-linecap="round">
    <path d="M2 6h7l6 24h22l5-17H12"/><circle cx="18" cy="38" r="3"/><circle cx="34" cy="38" r="3"/>
  </svg>
</header>

<section class="hero">
  <h1 class="abs hero-title">online farmers stand</h1>
  <h2 class="abs hero-sub">for local artisans</h2>
  <p class="abs hero-text">Lorem ipsum dolor sit amet, consectetur adipiscing elit, sed do eiusmod.</p>
  <div class="btn btn-outline-dark hero-btn">Shop Now</div>
  <div class="photo hero-photo" role="img" aria-label="Basket with fresh vegetables bursting out of it"></div>
  <div class="abs vertical hero-vertical">Farmers Stand</div>
  <div class="abs arrow" style="left:559px"><svg width="14" height="18" viewBox="0 0 14 18"><path d="M11 2L4 9l7 7" stroke="#fff" stroke-width="3" fill="none"/></svg></div>
  <div class="abs arrow" style="left:601px"><svg width="14" height="18" viewBox="0 0 14 18"><path d="M3 2l7 7-7 7" stroke="#fff" stroke-width="3" fill="none"/></svg></div>
</section>

<section class="promos">
  <div class="abs promo" style="left:55px">
    <div class="photo promo-heart" role="img" aria-label="Green vegetables arranged in a heart shape" style="border-radius:50% 50% 50% 50%/45% 45% 55% 55%;background:radial-gradient(circle,#7fb543 0%,#4f8a2a 60%,#2f6a1c 100%)"></div>
    <h3 class="abs promo-title">Fresh Organic</h3>
    <p class="abs promo-text">Sed ut perspiciatis unde omnis iste natus error sit voluptatem accusantium.</p>
    <div class="btn btn-outline-green">Shop Now</div>
  </div>
  <div class="abs promo" style="left:614px">
    <div class="photo promo-heart" role="img" aria-label="Colourful fruit and vegetables arranged in a heart shape" style="border-radius:50% 50% 50% 50%/45% 45% 55% 55%;background:radial-gradient(circle,#f0a13a 0%,#d83a2c 55%,#8a2a3a 100%)"></div>
    <h3 class="abs promo-title">Offer 10%</h3>
    <p class="abs promo-text">Sed ut perspiciatis unde omnis iste natus error sit voluptatem accusantium.</p>
    <div class="btn btn-outline-green">Shop Now</div>
  </div>
</section>

<section class="about">
  <div class="abs vertical about-vertical">Farmers Farm</div>
  <div class="photo about-photo" role="img" aria-label="Farmer holding a wooden crate of fresh vegetables"></div>
  <div class="abs about-box">
    <h2 class="abs about-title">About Us</h2>
    <p class="abs about-text">Sed ut perspiciatis unde omnis iste natus error sit voluptatem accusan­tium doloremque laudantium, totam rem aperiam, eaque ipsa quae ab illo inventore veritatis et quasi architecto beatae vitae dicta sunt explicabo. Nemo enim ipsam voluptatem quia voluptas sit aspernatur aut odit aut fugit, sed quia consequuntur magni dolores eos qui ratione voluptatem sequi nesciunt.</p>
    <div class="btn btn-outline-white">Sign Up</div>
  </div>
</section>

<section class="products">
  <h2 class="abs section-title">Our Products</h2>
  <div class="abs section-rule"></div>

  <svg width="0" height="0" style="position:absolute">
    <defs>
      <symbol id="star" viewBox="0 0 24 24"><path d="M12 1.5l3.1 6.6 7.2.9-5.3 5 1.4 7.1L12 17.6l-6.4 3.5 1.4-7.1-5.3-5 7.2-.9z" fill="#f28a1b"/></symbol>
    </defs>
  </svg>

  <div class="abs product" style="left:35px;top:2041px">
    <div class="photo product-photo" role="img" aria-label="Fresh broccoli" style="background:radial-gradient(circle,#5fa83a,#3a7d22 70%,#fff 71%)"></div>
    <h3 class="abs product-name">Fresh Broccoli</h3>
    <svg class="abs stars" width="150" height="26"><use href="#star" x="0" width="26" height="26"/><use href="#star" x="31" width="26" height="26"/><use href="#star" x="62" width="26" height="26"/><use href="#star" x="93" width="26" height="26"/><use href="#star" x="124" width="26" height="26"/></svg>
    <span class="abs price">5$</span>
    <div class="btn btn-outline-green">Shop Now</div>
  </div>
  <div class="abs product" style="left:416px;top:2041px">
    <div class="photo product-photo" role="img" aria-label="Strawberries" style="background:radial-gradient(circle,#e4403a,#b8221f 70%,#fff 71%)"></div>
    <h3 class="abs product-name">Strawberries</h3>
    <svg class="abs stars" width="150" height="26"><use href="#star" x="0" width="26" height="26"/><use href="#star" x="31" width="26" height="26"/><use href="#star" x="62" width="26" height="26"/><use href="#star" x="93" width="26" height="26"/><use href="#star" x="124" width="26" height="26"/></svg>
    <span class="abs price">5$</span>
    <div class="btn btn-outline-green">Shop Now</div>
  </div>
  <div class="abs product" style="left:795px;top:2041px">
    <div class="photo product-photo" role="img" aria-label="Red, yellow, orange and green bell peppers" style="background:linear-gradient(90deg,#d7261e,#f08a1a 45%,#f2c21c 60%,#3e7a24);border-radius:38%"></div>
    <h3 class="abs product-name">Bellpeppers</h3>
    <svg class="abs stars" width="150" height="26"><use href="#star" x="0" width="26" height="26"/><use href="#star" x="31" width="26" height="26"/><use href="#star" x="62" width="26" height="26"/><use href="#star" x="93" width="26" height="26"/><use href="#star" x="124" width="26" height="26"/></svg>
    <span class="abs price">5$</span>
    <div class="btn btn-outline-green">Shop Now</div>
  </div>

  <div class="abs product" style="left:35px;top:2519px">
    <div class="photo product-photo" role="img" aria-label="Pears" style="background:radial-gradient(circle,#c9c23a,#a4812b 70%,#fff 71%)"></div>
    <h3 class="abs product-name">Pear Fruits</h3>
    <svg class="abs stars" width="150" height="26"><use href="#star" x="0" width="26" height="26"/><use href="#star" x="31" width="26" height="26"/><use href="#star" x="62" width="26" height="26"/><use href="#star" x="93" width="26" height="26"/><use href="#star" x="124" width="26" height="26"/></svg>
    <span class="abs price">5$</span>
    <div class="btn btn-outline-green">Shop Now</div>
  </div>
  <div class="abs product" style="left:416px;top:2519px">
    <div class="photo product-photo" role="img" aria-label="Fresh lettuce" style="background:radial-gradient(circle,#b8e06a,#5fa83a 70%,#fff 71%)"></div>
    <h3 class="abs product-name">Fresh Lettuce</h3>
    <svg class="abs stars" width="150" height="26"><use href="#star" x="0" width="26" height="26"/><use href="#star" x="31" width="26" height="26"/><use href="#star" x="62" width="26" height="26"/><use href="#star" x="93" width="26" height="26"/><use href="#star" x="124" width="26" height="26"/></svg>
    <span class="abs price">5$</span>
    <div class="btn btn-outline-green">Shop Now</div>
  </div>
  <div class="abs product" style="left:795px;top:2519px">
    <div class="photo product-photo" role="img" aria-label="Oranges, one cut in half" style="background:radial-gradient(circle,#f9b640,#ee7d12 70%,#fff 71%)"></div>
    <h3 class="abs product-name">Orange Fruits</h3>
    <svg class="abs stars" width="150" height="26"><use href="#star" x="0" width="26" height="26"/><use href="#star" x="31" width="26" height="26"/><use href="#star" x="62" width="26" height="26"/><use href="#star" x="93" width="26" height="26"/><use href="#star" x="124" width="26" height="26"/></svg>
    <span class="abs price">5$</span>
    <div class="btn btn-outline-green">Shop Now</div>
  </div>
</section>

<section class="contact">
  <div class="abs contact-panel">
    <h2 class="abs contact-title">Contact Us</h2>
    <div class="abs field" style="top:155px">Name*</div>
    <div class="abs field" style="top:226px">Email Id*</div>
    <div class="abs field" style="top:296px">Phone no*</div>
    <div class="abs field" style="top:366px;height:100px">Your Message*</div>
    <div class="btn contact-btn">Shop Now</div>
  </div>
  <div class="abs contact-brand">Brindlecove</div>
  <p class="abs contact-line" style="top:3303px">Farmer's Stand</p>
  <p class="abs contact-line" style="top:3333px">Phone. XXX-XXX-XXXX</p>
  <p class="abs contact-line" style="top:3363px">Fax. XXX-XXX-XXXX</p>
  <p class="abs contact-line" style="top:3396px">Demo@brindlecove.com</p>
  <div class="abs social"><span></span><span></span><span></span><span></span><span></span><span></span><span></span></div>
  <div class="photo fruit-photo" role="img" aria-label="Bowl of mixed berries and sliced fruit spilling out"></div>
</section>

<footer class="abs footer">Brindlecove © 2018 All Rights Reserved | Privacy Policy</footer>

</body>
</html>
```